A poster for Vale Chiropractic's up coming powerful health workshop/seminar

I need a poster developed for Dr. Prent's upcoming Total Shape Reset and Armor Plating your Wellness seminar/workshop. This workshop will teach attendants how to shed pounds and rapidly reduce their waist size. Learn why weight loss doesn't work 99.9% of the time so that you can be the successful .1%. It's time to expose the LIES and reveal the TRUTH about the REAL causes of HEART DISEASE, DIABETES, CANCER, CHRONIC FATIGUE, ARTHRITIS, FIBROMYALGIA, and how to REVERSE/PREVENT this from ever happening to you or your family. The Insider Secrets to building your body into a health fortress unbreachable by sickness and disease. Learn to live and fufill your GOD-GIVEN health potential. Eliminate high bloodpressure, high cholesterol, diabetes, fatigue, chronic pain
Ending the WAR on sickness and disease by launching an unstoppable health offensive that will pummel any enemy of life and health.

I'm not a designer by any means, but was thinking of possible WAR theme, cammo, etc....just a thought. Not a requirement by any means
Updates

Dr. Prent has taken a look at all the submissions and has requested a few changes.

1. He wants the new map that has been added to the brief with Marlow Ridge College as a title above the map

2. He wants a section that describes what the attendees will gain at the seminar in bullet format.  Example:  Title....It's not about what you lose

                                                   I'ts about what you gain....

>The No-Hype, No- Gimmick  secrets for fast effective Weight loss

>How the top 3 disease killers, heart disease, cancer, and diabetes are linked to diet

>Tools and strategies to make 2012 the best year ever

The Seminar will be held at Marlow Ridge College, Tuesday January 3rd @ 6:30pm Open to Public

Target Market(s)

Adults 30-65

Industry/Entity Type

Building

Requirements
Should not have
• ruyrtur

```html
<!DOCTYPE html>
<html lang="en">
<head>
<meta charset="utf-8">
<title>Dr. Prent's Total Shape Reset Workshop</title>
<link rel="stylesheet" href="https://fonts.googleapis.com/css2?family=Arvo:wght@700&family=Great+Vibes&family=Michroma&display=swap">
<style>
  :root {
    --page: #ffffff;
    --panel: #000000;
    --panel-edge: #3a3a3a;
    --silver-hi: #ffffff;
    --silver-lo: #8a8a8a;
    --teal: #a9c7c0;
    --teal-glow: #2f8f86;
    --pink: #d89a9f;
    --pink-bright: #f0b8bd;
    --pink-deep: #b3616a;
    --pink-glow: #ff6f86;
    --body-white: #e9e9e9;
    --map-land: #3c4a44;
    --map-road: #6f7f77;
  }
  * { margin: 0; padding: 0; box-sizing: border-box; }
  html, body {
    width: 950px; height: 1200px; overflow: hidden;
    background: var(--page);
  }
  .poster {
    position: relative; width: 950px; height: 1200px;
    background: var(--page);
  }
  .panel {
    position: absolute; left: 52px; top: 5px; width: 841px; height: 1190px;
    background: var(--panel);
    border-radius: 38px;
    box-shadow: inset 0 0 0 3px var(--panel-edge), 0 0 6px rgba(0,0,0,.6);
  }
  .host-name {
    position: absolute; left: 78px; top: 92px;
    font-family: "Great Vibes", cursive;
    font-size: 78px; line-height: 1;
    color: #ffffff;
    -webkit-text-stroke: 2px #1a1a1a;
    text-shadow: 0 0 4px #fff, 2px 3px 0 #666;
    transform: rotate(-14deg);
    transform-origin: left bottom;
    white-space: nowrap;
  }
  .title-lead {
    position: absolute; left: 428px; top: 68px;
    font-family: "Arvo", serif; font-weight: 700;
    font-size: 88px; line-height: 1; letter-spacing: 1px;
    background: linear-gradient(180deg, var(--silver-hi) 25%, var(--silver-lo) 100%);
    -webkit-background-clip: text; background-clip: text; color: transparent;
    filter: drop-shadow(0 0 6px rgba(255,255,255,.55));
  }
  .title-line {
    position: absolute; left: 52px; width: 841px; text-align: center;
    font-family: "Arvo", serif; font-weight: 700;
    font-size: 48px; line-height: 1;
    color: var(--teal);
    text-shadow: 0 0 10px var(--teal-glow), 0 0 3px #fff;
    white-space: nowrap;
  }
  .title-line.second { top: 170px; padding-left: 10px; }
  .title-line.third { top: 222px; padding-left: 40px; }
  .event-type {
    position: absolute; left: 52px; width: 841px; top: 268px; text-align: center;
    font-family: "Arvo", serif; font-weight: 700;
    font-size: 118px; line-height: 1; letter-spacing: -1px;
    color: var(--pink);
    -webkit-text-stroke: 2px var(--pink-deep);
    text-shadow: 0 0 16px var(--pink-glow), 0 0 4px #fff;
  }
  .presenter-photo {
    position: absolute; left: 140px; top: 340px; width: 150px; height: 400px;
    border-radius: 60px 60px 8px 8px;
    background: linear-gradient(180deg, #2a2a2a 0%, #141414 40%, #0b0b0b 100%);
  }
  .tone-fade {
    position: absolute; left: 280px; top: 390px; width: 220px; height: 360px;
    background: radial-gradient(ellipse at 40% 50%, rgba(120,120,120,.35), rgba(0,0,0,0) 70%);
  }
  .copy {
    position: absolute;
    font-family: "Michroma", sans-serif;
    text-transform: uppercase;
    text-align: center;
  }
  .copy strong { font-weight: 400; color: var(--pink-bright); }
  .intro-copy {
    left: 300px; top: 404px; width: 560px;
    font-size: 15px; line-height: 22.4px; letter-spacing: 3px;
    color: var(--pink);
  }
  .secrets-copy {
    left: 84px; top: 760px; width: 396px;
    font-size: 11px; line-height: 15.4px; letter-spacing: 2.6px;
    color: var(--body-white);
  }
  .secrets-copy strong { color: #ffffff; }
  .result-photo {
    position: absolute; left: 496px; top: 748px; width: 372px; height: 240px;
    border: 6px solid #f2f2f2;
    transform: rotate(2.5deg);
    background: linear-gradient(180deg, #a9c7dc 0%, #d9cfc3 45%, #d9a48b 100%);
    box-shadow: 0 2px 8px rgba(0,0,0,.7);
  }
  .time-place {
    position: absolute; left: 52px; width: 841px; top: 1006px; text-align: center;
    font-family: "Michroma", sans-serif;
    font-size: 38px; line-height: 1; letter-spacing: 3px;
    background: linear-gradient(180deg, #ffffff 20%, #7c7c7c 100%);
    -webkit-background-clip: text; background-clip: text; color: transparent;
  }
  .gain {
    position: absolute; left: 84px; top: 1058px; width: 390px;
  }
  .gain-title {
    font-family: "Arvo", serif; font-weight: 700;
    font-size: 15px; line-height: 18px; color: var(--teal);
  }
  .gain-subtitle {
    font-family: "Arvo", serif; font-weight: 700;
    font-size: 15px; line-height: 18px; color: var(--pink);
    margin-bottom: 4px;
  }
  .gain-list { list-style: none; }
  .gain-list li {
    position: relative; padding-left: 14px;
    font-family: "Michroma", sans-serif;
    font-size: 9px; line-height: 12.5px; letter-spacing: .6px;
    color: var(--body-white); text-transform: uppercase;
    margin-bottom: 3px;
  }
  .gain-list li::before {
    content: ""; position: absolute; left: 0; top: 3px;
    border-left: 7px solid var(--pink); border-top: 4px solid transparent; border-bottom: 4px solid transparent;
  }
  .venue {
    position: absolute; left: 496px; top: 1058px; width: 372px;
  }
  .venue-title {
    font-family: "Arvo", serif; font-weight: 700;
    font-size: 15px; line-height: 18px; color: var(--teal);
    text-align: center; margin-bottom: 4px;
  }
  .venue-map { display: block; width: 372px; height: 64px; }
  .venue-details {
    margin-top: 6px;
    font-family: "Michroma", sans-serif;
    font-size: 9px; line-height: 12px; letter-spacing: .6px;
    color: var(--pink); text-align: center; text-transform: uppercase;
  }
</style>
</head>
<body>
<div class="poster">
  <div class="panel"></div>

  <div class="tone-fade"></div>

  <div class="host-name">Dr. Prent's</div>
  <div class="title-lead">Total</div>
  <div class="title-line second">Shape Reset and</div>
  <div class="title-line third">Armor Plating your Wellness</div>
  <div class="event-type">workshop</div>

  <div class="presenter-photo" role="img" aria-label="Photo of Dr. Prent standing in a dark suit"></div>

  <p class="copy intro-copy">This workshop will teach attendants how to shed pounds and rapidly reduce their waist size. Learn why weight loss doesn't work 99.9% of the time so that you can be the successful .1%. It's time to expose the <strong>LIES</strong> and reveal the <strong>TRUTH</strong> about the <strong>REAL</strong> causes of <strong>HEART DISEASE, DIABETES, CANCER, CHRONIC FATIGUE, ARTHRITIS, FIBROMYALGIA,</strong> and how to <strong>REVERSE/PREVENT</strong> this from ever happening to you or your family.</p>

  <div class="result-photo" role="img" aria-label="Photo of a slim waist being measured with a pink tape measure"></div>

  <p class="copy secrets-copy">The Insider Secrets to building your body into a health fortress unbreachable by sickness and disease. Learn to live and fufill your <strong>GOD-GIVEN</strong> health potential. Eliminate high bloodpressure, high cholesterol, diabetes, fatigue, chronic pain. Ending the <strong>WAR</strong> on sickness and disease by launching an unstoppable health offensive that will pummel any enemy of life and health.</p>

  <div class="time-place">TIME AND PLACE</div>

  <section class="gain">
    <h2 class="gain-title">It's not about what you lose&hellip;</h2>
    <p class="gain-subtitle">It's about what you gain&hellip;</p>
    <ul class="gain-list">
      <li>The No-Hype, No-Gimmick secrets for fast effective weight loss</li>
      <li>How the top 3 disease killers, heart disease, cancer and diabetes are linked to diet</li>
      <li>Tools and strategies to make 2012 the best year ever</li>
    </ul>
  </section>

  <section class="venue">
    <h2 class="venue-title">Marlow Ridge College</h2>
    <svg class="venue-map" viewBox="0 0 372 64" role="img" aria-label="Map showing the way to Marlow Ridge College">
      <rect width="372" height="64" rx="4" fill="var(--map-land)"/>
      <path d="M0 40 H372 M120 0 V64 M250 0 L300 64" stroke="var(--map-road)" stroke-width="5" fill="none"/>
      <circle cx="185" cy="30" r="7" fill="var(--pink)"/>
    </svg>
    <p class="venue-details">Tuesday January 3rd @ 6:30pm &middot; Open to Public</p>
  </section>
</div>
</body>
</html>
```